Psychologist in Private Practice Needs a Website Update

Project Description:
Hello talented designers! My current website, www.jodelbrisk.com, needs a fresh, boho-modern makeover that highlights the warm, welcoming nature of my holistic therapy practice. I want a website that has a serene, boho- modern design, appealing to clients seeking individual therapy, couples therapy, and family counseling.

I’d also like to prepare for a future second site focused exclusively on couples and family therapy. Both sites should be interconnected, so I’m looking for design suggestions that seamlessly link them together while maintaining a cohesive brand look and feel.

Key Objectives:

Boho-Modern Aesthetic: Incorporate natural textures, neutral or earthy tones, and clean lines that capture a modern, inviting vibe.

Responsive Design: Ensure the website is user-friendly on desktop, tablet, and mobile devices.

Clear Service Offerings: Prominently feature my three distinct services: individual therapy, couples therapy, and family counseling.

Interlinked Future Site: Provide ideas on how to cross-link this site with a second site focused on couples and family therapy.

User Experience (UX): Make the site simple to navigate, with intuitive placement of content that speaks to potential clients’ needs.

SEO-Friendly: Implement best practices for structure, site speed, and keyword usage to boost online visibility.

What I Have Now:
Existing website: www.jodelbrisk.com
Basic content and a logo that can be refined or updated to match the boho-modern feel
Rough style guide with brand elements open to a fresh interpretation

Preferred Style/Tone:
Boho-modern with earthy tones, subtle textures, and clean typography
Warm, empathetic, and approachable to align with the nature of therapy services
Slightly artistic or organic elements that evoke calm and connection

Potential for an ongoing design relationship!
Updates

Need extra days to review

Target Market(s)

I have a high functioning, professional clientele who doctors, lawyers, and leaders in their field.

Industry/Entity Type

healthcare/mental health

Coding

Coded - Design and coding required

Font styles to use
Other font styles liked:
• cormorant garamond for headers and Source Sans Pro for supporting text

Colors

Designer to choose colors to be used in the design.

Requirements
Must have
• Open, Harmonious Layout I’d like the overall design to feel upscale, humanistic, open and harmonious, with minimal divisions of space. Rather than traditional section dividers, please consider using images, subtle shifts in color, typography, or spacing to define sections. Hero Image & Inspiration Ideally, the first (hero) image should evoke a sense of awe or inspiration. Focus on simplicity and elegance so the design feels spacious and inviting, allowing the content and imagery to really stand out. Natural Flow Wherever possible, let the design elements flow naturally into each other, creating a sense of unity and cohesion throughout the site.
Nice to have
• 1. Full-Width Hero Image: • The homepage should feature a full-width hero image that extends edge-to-edge across the screen for a modern and visually immersive effect. • This image should set the tone for the website, reflecting a calming, humanistic/natural, and upscale feel. It could include subtle overlays or gradients to enhance readability of text and navigation elements. Ideally, this image should have one or two people in nature. The image could be slightly transparent to allow the text "holistic therapy" and the tagline "an integrative approach to transformation" to be easily visible. Please help me find a breath-taking image that evokes a sense of beauty, inspiration, awe or hope. 2. Menu Tabs Positioned Over the Image: • The menu tabs (navigation bar) should be positioned directly on top of the hero image, either centered or aligned to the top right/left, depending on the design. • The navigation bar should have a slightly transparent or solid background (depending on the image and visibility needs) to ensure the text is easily readable without detracting from the image. 3. Typography and Text Placement: • The text overlay on the hero image should use the selected fonts: • Cormorant Garamond for headers (e.g., the tagline or welcome message). • Source Sans Pro for any supporting text. 5. Seamless Transitions: • Below the full-width image, transitions into the next sections (like “About,” “Services,” or client-focused content) should be smooth, using full-width separators that maintain the cohesive, open layout style. 6. Color Palette: • A neutral and calming color palette should be used (e.g., soft blues, grays, whites, or very muted earth tones) to create a soothing atmosphere for visitors. This design approach ensures the homepage looks clean, modern, and professional while maintaining the calming and upscale aesthetic that reflects the values of my psychology practice

```html
<!DOCTYPE html>
<html lang="en">
<head>
<meta charset="utf-8">
<title>Dr. Jodel Brisk – Licensed Psychologist</title>
<link href="https://fonts.googleapis.com/css2?family=Italiana&family=Lato:wght@400;700&family=Great+Vibes&display=swap" rel="stylesheet">
<style>
:root{
  --cream:#f7ede4;
  --sand:#f1e0d0;
  --clay:#b08169;
  --rust:#b06a2e;
  --ink:#2b2522;
  --muted:#5a4f49;
  --footer:#bfa78f;
  --line:#d9c3b0;
}
*{box-sizing:border-box;margin:0;padding:0}
html,body{width:1200px;height:4525px;overflow:hidden}
body{position:relative;background:var(--cream);font-family:'Lato',sans-serif;color:var(--ink)}
.abs{position:absolute}
.display{font-family:'Italiana',serif;font-weight:400;color:var(--ink);line-height:1}
.eyebrow{font-size:13px;letter-spacing:4px;color:var(--rust);font-weight:700}
.btn{position:absolute;display:flex;align-items:center;justify-content:center;background:var(--rust);color:#fff;font-size:11px;letter-spacing:2px;font-weight:700}
.btn-outline{background:transparent;border:1.5px solid var(--rust);color:var(--rust)}
.photo{position:absolute}
p.body{font-size:15px;line-height:28.5px;color:var(--muted)}

.topbar{top:0;left:0;width:1200px;height:42px;background:var(--sand);border-bottom:1px solid var(--line);font-size:12px;color:var(--ink)}
.topbar span{position:absolute;top:14px;display:flex;align-items:center;gap:6px}
.header{top:42px;left:0;width:1200px;height:86px;background:var(--sand)}
.brand{position:absolute;left:84px;top:15px;display:flex;align-items:center;gap:12px}
.brand-dot{width:58px;height:58px;border-radius:50%;background:#d9b37a}
.brand-name{font-size:22px;line-height:22px;color:var(--ink)}
.brand-name small{display:block;font-size:17px}
.nav{position:absolute;top:31px;font-size:12px;letter-spacing:1.5px;color:var(--ink)}
.nav.active{border-bottom:1px solid var(--ink);padding-bottom:3px}

.hero{top:128px;left:0;width:1200px;height:531px;background:var(--sand)}
.hero-line{left:622px;font-family:'Italiana',serif;color:var(--ink);white-space:nowrap}

.services{top:1316px;left:0;width:1200px;height:659px;background:var(--clay)}
.card{position:absolute;top:190px;width:315px;height:400px;border:1.5px solid #e2c6b4;border-radius:158px 158px 0 0}
.card .photo{left:15px;top:16px;width:283px;height:340px;border-radius:142px 142px 0 0}
.card span{position:absolute;bottom:10px;width:100%;text-align:center;color:#fff;font-size:20px;letter-spacing:.5px}

.field{position:absolute;border:1px solid #9c8f86;font-size:14px;color:var(--muted);padding:14px 8px}

.faq{top:2632px;left:0;width:1200px;height:763px;background:var(--sand)}
.faq-row{position:absolute;left:311px;width:578px;height:60px;display:flex;align-items:center;font-size:26px;color:var(--ink)}
.faq-row b{font-weight:400;width:88px;padding-left:25px;font-size:28px}
.faq-rule{position:absolute;left:311px;width:578px;border-top:1px solid #c9b3a0}

.footer{top:4053px;left:0;width:1200px;height:472px;background:var(--footer);color:#fff}
.footer h4{position:absolute;top:85px;font-family:'Italiana',serif;font-weight:400;font-size:24px;color:#fff}
.footer .small{font-size:12.5px;line-height:24px;color:#fff}
.links a{display:block;color:#fff;text-decoration:none;font-size:12.5px;height:32.5px}
.social{position:absolute;top:236px;width:18px;height:18px;border:2px solid #fff;border-radius:3px}
</style>
</head>
<body>

<div class="abs topbar">
  <span style="left:84px">
    <svg width="11" height="14" viewBox="0 0 11 14"><path d="M5.5 0C2.5 0 0 2.4 0 5.4 0 9.3 5.5 14 5.5 14S11 9.3 11 5.4C11 2.4 8.5 0 5.5 0zm0 7.6a2.2 2.2 0 110-4.4 2.2 2.2 0 010 4.4z" fill="#b06a2e"/></svg>
    418 Linden Hollow Road, Fernbrook MD 20917</span>
  <span style="left:842px">
    <svg width="12" height="12" viewBox="0 0 24 24"><path d="M6.6 10.8a15.1 15.1 0 006.6 6.6l2.2-2.2c.3-.3.7-.4 1-.2 1.1.4 2.3.6 3.6.6.6 0 1 .4 1 1V20c0 .6-.4 1-1 1A17 17 0 013 4c0-.6.4-1 1-1h3.5c.6 0 1 .4 1 1 0 1.3.2 2.5.6 3.6.1.3 0 .7-.2 1z" fill="#b06a2e"/></svg>
    (410) 555-0187</span>
  <span style="left:958px">
    <svg width="13" height="10" viewBox="0 0 13 10"><rect width="13" height="10" rx="1" fill="#b06a2e"/><path d="M0 1l6.5 4.5L13 1" stroke="#f1e0d0" fill="none"/></svg>
    drjodelbrisk@mailbox.net</span>
</div>

<div class="abs header">
  <div class="brand"><div class="brand-dot"></div><div class="brand-name">Dr. Jodel Brisk<small>Licensed Psychologist</small></div></div>
  <div class="nav active" style="left:502px">HOME</div>
  <div class="nav" style="left:599px">ABOUT</div>
  <div class="nav" style="left:701px">SERVICES ▾</div>
  <div class="nav" style="left:820px">FAQS</div>
  <div class="nav" style="left:912px">BLOG</div>
  <div class="btn" style="left:972px;top:18px;width:142px;height:47px">CONTACT</div>
</div>

<section class="abs hero">
  <div class="photo" role="img" aria-label="Soft-focus pampas grass beside a warm wooden curve" style="left:0;top:0;width:485px;height:531px;background:linear-gradient(120deg,#8a4a25 0%,#b98a63 22%,#e6d6c6 45%,#cdbcae 75%,#a89686 100%)"></div>
  <div class="photo" style="left:357px;top:144px;width:226px;height:276px;border-radius:113px 113px 0 0;background:#c9b8a8;border:3px solid #f1e0d0"></div>
  <div class="photo" role="img" aria-label="Portrait photo of Dr. Jodel Brisk" style="left:364px;top:151px;width:212px;height:269px;border-radius:106px 106px 0 0;background:linear-gradient(180deg,#b7a596,#8c6a4f 60%,#5a4438)"></div>
  <div class="abs hero-line" style="top:66px;font-size:28px">We offer therapy for individuals</div>
  <div class="abs hero-line" style="top:106px;font-size:70px">Couples and</div>
  <div class="abs hero-line" style="top:196px;font-size:70px">Families to help</div>
  <div class="abs hero-line" style="top:283px;font-size:34px">you create meaningful change</div>
  <div class="btn" style="left:620px;top:353px;width:160px;height:46px">GET STARTED</div>
  <div class="abs" style="left:980px;top:492px;font-size:11px;letter-spacing:1.5px;color:#8a7a70">← PREV &nbsp;&nbsp;|&nbsp;&nbsp; <span style="color:var(--rust)">NEXT →</span></div>
</section>

<section class="abs" style="top:659px;left:0;width:1200px;height:657px">
  <div class="abs eyebrow" style="left:84px;top:149px">ABOUT</div>
  <h1 class="abs display" style="left:82px;top:170px;font-size:62px">Dr. Jodel Brisk</h1>
  <div class="abs" style="left:84px;top:241px;font-size:20px;font-style:italic;color:var(--ink)">Owner, Licensed Clinical Psychologist</div>
  <p class="abs body" style="left:84px;top:283px;width:460px">I earned my Doctor of Psychology (Psy.D.) in Clinical Psychology from Harborview University. In addition to my private practice in West Fernbrook, I am also the Director of Counseling at Linden College, where I oversee all aspects of counseling services, including outreach programming.</p>
  <div class="btn" style="left:84px;top:487px;width:202px;height:45px">LITTLE MORE ABOUT ME</div>
  <div class="photo" role="img" aria-label="Portrait photo of Dr. Jodel Brisk" style="left:673px;top:88px;width:402px;height:469px;border-radius:201px 201px 0 0;background:linear-gradient(180deg,#4a4238,#7b5b43 45%,#3d302a)"></div>
  <div class="abs" style="left:705px;top:525px;font-family:'Great Vibes',cursive;font-size:78px;color:var(--rust)">Jodel Brisk</div>
</section>

<section class="abs services">
  <div class="abs eyebrow" style="left:0;width:1200px;text-align:center;top:82px;color:#fff">SERVICES</div>
  <h2 class="abs display" style="left:0;width:1200px;text-align:center;top:104px;font-size:62px;color:#fff">How Can I Help You</h2>
  <div class="card" style="left:84px"><div class="photo" role="img" aria-label="Therapist with an individual client on a sofa" style="background:linear-gradient(180deg,#e7e4e2,#bfb5ae 60%,#3a3230)"></div><span>INDIVIDUAL THERAPY</span></div>
  <div class="card" style="left:443px"><div class="photo" role="img" aria-label="Therapist with a couple on a sofa" style="background:linear-gradient(180deg,#efeeec,#d6cfc8 60%,#8e7b6d)"></div><span>COUPLES THERAPY</span></div>
  <div class="card" style="left:801px"><div class="photo" role="img" aria-label="Therapist with a family on a sofa" style="background:linear-gradient(180deg,#dcdad3,#bba89a 55%,#4b4a4c)"></div><span>FAMILY COUNSELING</span></div>
</section>

<section class="abs" style="top:1975px;left:0;width:1200px;height:657px">
  <div class="photo" role="img" aria-label="Person meditating on a wooden dock at sunset over a lake" style="left:135px;top:81px;width:403px;height:469px;border-radius:201px 201px 0 0;background:linear-gradient(180deg,#f7c9a0,#e8a36c 45%,#b66c3e 65%,#4a2a1c)"></div>
  <div class="abs eyebrow" style="left:613px;top:134px">CONTACT</div>
  <h2 class="abs display" style="left:611px;top:154px;font-size:62px">Get In Touch</h2>
  <div class="abs" style="left:614px;top:219px;font-size:20px;color:var(--ink)">Have more questions? <b>Reach out today!</b></div>
  <div class="field" style="left:613px;top:262px;width:244px;height:47px">Name</div>
  <div class="field" style="left:868px;top:262px;width:246px;height:47px">Email</div>
  <div class="field" style="left:613px;top:323px;width:501px;height:139px">How can i help you...</div>
  <div class="btn" style="left:613px;top:478px;width:134px;height:45px">SUBMIT</div>
</section>

<section class="abs faq">
  <h2 class="abs display" style="left:0;width:1200px;text-align:center;top:70px;font-size:62px">Frequently Asked Questions</h2>
  <div class="faq-row" style="top:151px"><b>+</b>Where are you located?</div>
  <div class="faq-rule" style="top:216px"></div>
  <div class="faq-row" style="top:228px"><b>+</b>What states do you offer telehealth in?</div>
  <div class="faq-rule" style="top:299px"></div>
  <div class="faq-row" style="top:311px"><b>+</b>What types of clients do you see?</div>
  <div class="faq-rule" style="top:378px"></div>
  <div class="faq-row" style="top:390px"><b>+</b>Do you take insurance?</div>
  <div class="faq-rule" style="top:464px"></div>
  <div class="faq-row" style="top:476px"><b>+</b>How do out of network benefits work?</div>
  <div class="faq-rule" style="top:548px"></div>
  <div class="faq-row" style="top:560px"><b>+</b>What can I expect in my first session?</div>
  <div class="btn btn-outline" style="left:478px;top:657px;width:244px;height:46px">VIEW ALL QUESTION ANSWER</div>
</section>

<section class="abs" style="top:3395px;left:0;width:1200px;height:658px">
  <div class="abs" style="left:775px;top:0;width:425px;height:658px;background:var(--clay)"></div>
  <div class="abs eyebrow" style="left:86px;top:90px">BLOG</div>
  <h2 class="abs display" style="left:84px;top:112px;font-size:62px">Blog posts</h2>
  <h3 class="abs" style="left:86px;top:207px;width:420px;font-size:24px;line-height:33px;font-weight:700;color:var(--ink)">Communication in Relationships: Getting to the Heart of the Issue</h3>
  <p class="abs body" style="left:86px;top:287px;width:390px">When couples say communication in relationships is their primary problem, they are missing opportunities to truly learn to understand each other. Often, there are underlying emotions that drive “communication issues.” Unfortunately, we are not always aware of the underlying emotions for ourselves or our partner.</p>
  <div class="btn" style="left:86px;top:485px;width:151px;height:45px">LEARN MORE</div>
  <div class="photo" role="img" aria-label="Lone tree standing in still water under a pink and violet sky" style="left:562px;top:79px;width:447px;height:502px;border-radius:224px 224px 0 0;background:linear-gradient(180deg,#4f5fb8,#b87bb8 40%,#e79bb0 55%,#6b62a6 75%,#3e3d7a)"></div>
</section>

<footer class="abs footer">
  <h4 style="left:86px">Info</h4>
  <p class="abs small" style="left:86px;top:140px;width:240px">It can be intimidating to reach out for help, especially if you have never been to therapy before. We are committed to making the process as smooth and simple as we can.</p>
  <h4 style="left:394px">Contact Info</h4>
  <div class="abs small" style="left:394px;top:140px;width:240px;display:flex;gap:14px">
    <svg width="11" height="14" viewBox="0 0 11 14" style="flex:none;margin-top:5px"><path d="M5.5 0C2.5 0 0 2.4 0 5.4 0 9.3 5.5 14 5.5 14S11 9.3 11 5.4C11 2.4 8.5 0 5.5 0zm0 7.6a2.2 2.2 0 110-4.4 2.2 2.2 0 010 4.4z" fill="#fff"/></svg>
    <span>418 Linden Hollow Road, Fernbrook MD 20917</span></div>
  <div class="abs small" style="left:394px;top:195px;display:flex;gap:12px;align-items:center">
    <svg width="13" height="13" viewBox="0 0 24 24"><path d="M6.6 10.8a15.1 15.1 0 006.6 6.6l2.2-2.2c.3-.3.7-.4 1-.2 1.1.4 2.3.6 3.6.6.6 0 1 .4 1 1V20c0 .6-.4 1-1 1A17 17 0 013 4c0-.6.4-1 1-1h3.5c.6 0 1 .4 1 1 0 1.3.2 2.5.6 3.6.1.3 0 .7-.2 1z" fill="none" stroke="#fff" stroke-width="2"/></svg>
    (410) 555-0187</div>
  <div class="abs small" style="left:394px;top:227px;display:flex;gap:12px;align-items:center">
    <svg width="13" height="10" viewBox="0 0 13 10"><rect x=".5" y=".5" width="12" height="9" rx="1" fill="none" stroke="#fff"/><path d="M.5 1l6 4.5 6-4.5" stroke="#fff" fill="none"/></svg>
    drjodelbrisk@mailbox.net</div>
  <h4 style="left:687px">Quick Links</h4>
  <nav class="abs links" style="left:687px;top:140px">
    <a href="#" style="font-weight:700;text-decoration:underline">Home</a><a href="#">About</a><a href="#">Services</a><a href="#">FAQs</a><a href="#">Blog</a><a href="#">Contact</a>
  </nav>
  <div class="abs" style="left:868px;top:139px;display:flex;align-items:center;gap:12px">
    <div style="width:64px;height:64px;border-radius:50%;background:#d9b37a"></div>
    <div style="font-size:22px;line-height:22px">Dr. Jodel Brisk<span style="display:block;font-size:17px">Licensed Psychologist</span></div>
  </div>
  <div class="social" style="left:968px"></div>
  <div class="social" style="left:1010px"></div>
  <div class="social" style="left:1050px"></div>
  <div class="abs" style="left:0;width:1200px;text-align:center;top:421px;font-size:11px">© 2025 <b>Dr. Jodel Brisk</b>. All right reserved</div>
</footer>

</body>
</html>
```